Velmora business card design

Design a business card for a cryptocurrency company that uses the attached logo. Some example business cards to give you guys a flavor of what we're looking for is given below (of course feel free to be creative):
https://www.plimtorque.com/studio.aspx?template=5813490_KT4&ag=True&xnav=HSG_Design_Image&rd=1
https://www.plimtorque.com/studio.aspx?template=7240615_KT4&ag=True&xnav=HSG_Design_Image&rd=1
The business card should be clean/simple and convey the company name, what we're about and the specific persons contact info. In terms of what we're about, we can have our name Velmora, with a line under it that says "Cryptocurrency visualization, analytics, and trading"
We want something futuristic looking but simple / clean.
The color scheme for the logo should be used.
The name of the person and their title should be editable, so we can use the business card design for multiple people.
(Please use the zip file to get the vector graphics and different image formats)

```html
<!DOCTYPE html>
<html lang="en">
<head>
<meta charset="utf-8">
<title>Velmora business card</title>
<link rel="stylesheet" href="https://fonts.googleapis.com/css2?family=Didact+Gothic&family=Montserrat:wght@600&family=Oswald:wght@400;500&display=swap">
<style>
  :root {
    --backdrop: #e4e1dc;
    --card-light: #ededed;
    --navy: #10213a;
    --ink: #3a3f47;
    --brand-blue: #2b8fe3;
    --brand-green: #1fd68a;
    --brand-teal: #16b9a6;
    --white: #ffffff;
  }
  * { margin: 0; padding: 0; box-sizing: border-box; }
  html, body { width: 1200px; height: 960px; overflow: hidden; }
  body { background: var(--backdrop); position: relative; }

  .card { position: absolute; border-radius: 22px; overflow: hidden; }
  .card--front { left: 315px; top: 130px; width: 600px; height: 340px; background: var(--card-light); }
  .card--back { left: 312px; top: 488px; width: 598px; height: 342px; background: var(--navy); }

  .brand { position: absolute; display: flex; align-items: center; gap: 14px; }
  .brand__mark { display: block; width: 18px; height: 18px; background: var(--brand-teal); }
  .brand__name {
    font-family: "Montserrat", sans-serif; font-weight: 600;
    letter-spacing: 2px; line-height: 1;
  }
  .card--front .brand { left: 53px; top: 75px; }
  .card--front .brand__name { font-size: 36px; color: var(--navy); }
  .card--back .brand { left: 0; right: 0; top: 150px; justify-content: center; }
  .card--back .brand__mark { width: 26px; height: 26px; }
  .card--back .brand__name { font-size: 46px; color: var(--brand-green); }

  .contact { position: absolute; left: 52px; top: 206px; list-style: none; }
  .contact__item {
    display: flex; align-items: center; gap: 7px; height: 19.2px;
    font-family: "Didact Gothic", sans-serif; font-size: 15px; color: var(--ink);
  }
  .contact__icon { width: 11px; height: 11px; fill: var(--navy); flex: none; }

  .person {
    position: absolute; left: 409px; top: 203px; width: 191px; height: 82px;
    background: var(--navy); padding: 14px 0 0 19px;
    font-family: "Oswald", sans-serif;
  }
  .person__name { font-size: 26px; font-weight: 500; color: var(--brand-blue); line-height: 1.05; letter-spacing: 0.3px; }
  .person__title { font-size: 15px; font-weight: 400; color: var(--brand-green); margin-left: 25px; letter-spacing: 0.6px; }

  .tagline {
    position: absolute; left: 0; right: 0; top: 284px; text-align: center;
    font-family: "Oswald", sans-serif; font-size: 13px; letter-spacing: 0.6px;
    color: var(--white); text-transform: uppercase;
  }
</style>
</head>
<body>
  <section class="card card--front">
    <div class="brand">
      <span class="brand__mark"></span>
      <span class="brand__name">VELMORA</span>
    </div>

    <ul class="contact">
      <li class="contact__item">
        <svg class="contact__icon" viewBox="0 0 24 24"><path d="M6.6 10.8a15.1 15.1 0 0 0 6.6 6.6l2.2-2.2c.3-.3.7-.4 1-.2 1.1.4 2.3.6 3.6.6.6 0 1 .4 1 1V20c0 .6-.4 1-1 1A17 17 0 0 1 3 4c0-.6.4-1 1-1h3.5c.6 0 1 .4 1 1 0 1.3.2 2.5.6 3.6.1.3 0 .7-.2 1z"/></svg>
        415 555 0192
      </li>
      <li class="contact__item">
        <svg class="contact__icon" viewBox="0 0 24 24"><path d="M7 1h10a2 2 0 0 1 2 2v18a2 2 0 0 1-2 2H7a2 2 0 0 1-2-2V3a2 2 0 0 1 2-2zm0 3v14h10V4zm5 15.5a1.2 1.2 0 1 0 0 2.4 1.2 1.2 0 0 0 0-2.4z"/></svg>
        415 555 0147
      </li>
      <li class="contact__item">
        <svg class="contact__icon" viewBox="0 0 24 24"><path d="M2 5h20v14H2zm2 2v.5l8 5 8-5V7zm0 3v7h16v-7l-8 5z"/></svg>
        daniel@velmora.com
      </li>
      <li class="contact__item">
        <svg class="contact__icon" viewBox="0 0 24 24"><path d="M12 2a10 10 0 1 0 0 20 10 10 0 0 0 0-20zm6.9 6h-3a15.7 15.7 0 0 0-1.4-3.6A8 8 0 0 1 18.9 8zM12 4c.8 1.2 1.5 2.5 1.9 4h-3.8c.4-1.5 1.1-2.8 1.9-4zM4.3 14a8.2 8.2 0 0 1 0-4h3.4a16.5 16.5 0 0 0 0 4zm.8 2h3a15.7 15.7 0 0 0 1.4 3.6A8 8 0 0 1 5.1 16zm3-8h-3a8 8 0 0 1 4.4-3.6C8.9 5.5 8.4 6.7 8.1 8zM12 20c-.8-1.2-1.5-2.5-1.9-4h3.8c-.4 1.5-1.1 2.8-1.9 4zm2.3-6H9.7a14.7 14.7 0 0 1 0-4h4.6a14.7 14.7 0 0 1 0 4zm.2 5.6c.6-1.1 1.1-2.3 1.4-3.6h3a8 8 0 0 1-4.4 3.6zm1.8-5.6a16.5 16.5 0 0 0 0-4h3.4a8.2 8.2 0 0 1 0 4z"/></svg>
        www.velmora.com
      </li>
    </ul>

    <div class="person">
      <p class="person__name">DANIEL REYES</p>
      <p class="person__title">CEO/FOUNDER</p>
    </div>
  </section>

  <section class="card card--back">
    <div class="brand">
      <span class="brand__mark"></span>
      <span class="brand__name">VELMORA</span>
    </div>
    <p class="tagline">Cryptocurrency visualization, analytics, &amp; trading</p>
  </section>
</body>
</html>
```